Glidewell Depot logo

Glidewell Depot is owned and operated by industry professionals with years of direct experience in providing customers with the right equipment to suit their needs. Our specialty lies within dealing in the Halvern Medical range of products. Our product range is suited to both the new user and for those that know what they want, a full line of products ranging from ultra-light wheelchairs, wheelchairs for sport and recreation and paediatric or just everyday use.

Industry/Entity Type

Recreation

Contact Information for Business Card

name, title, landline,fax,mobile,email,web address,physical address,logo,possibly a wheelchair pic

Requirements
Must have
• logo - uploaded
Nice to have
• colour scheme consistent with
www.glidewelldepot.com.au

```html
<!DOCTYPE html>
<html lang="en">
<head>
<meta charset="utf-8">
<title>Glidewell Depot – Business Card</title>
<link rel="stylesheet" href="https://fonts.googleapis.com/css2?family=Fira+Sans:wght@400;600&display=swap">
<style>
  :root {
    --backdrop: #2f3e47;
    --card-white: #ffffff;
    --ink: #1f1f1f;
    --accent-light: #4f94c9;
    --accent-blue: #0c5592;
    --accent-purple: #561c59;
    --photo-light: #f6f6f6;
    --photo-edge: #e6e6e6;
    --photo-silver: #a7a7a7;
    --photo-charcoal: #4a4a4c;
  }
  * { box-sizing: border-box; margin: 0; padding: 0; }
  html, body {
    width: 1200px; height: 1000px; overflow: hidden;
    background: var(--backdrop);
    font-family: "Fira Sans", Arial, sans-serif;
  }
  .stage { position: relative; width: 1200px; height: 1000px; }
  .card {
    position: absolute; left: 300px; width: 600px;
    border-radius: 22px; overflow: hidden;
    box-shadow: 0 4px 6px rgba(0,0,0,0.35);
  }
  .card-front { top: 136px; height: 342px; }
  .front-photo {
    width: 100%; height: 100%;
    background:
      radial-gradient(ellipse 70% 60% at 50% 50%, rgba(255,255,255,0) 60%, rgba(0,0,0,0.06) 100%),
      linear-gradient(180deg,
        var(--photo-light) 0%,
        var(--photo-light) 18%,
        var(--photo-silver) 28%,
        var(--photo-charcoal) 40%,
        #5c5c5e 55%,
        var(--photo-silver) 68%,
        #d8d8d8 80%,
        var(--photo-light) 86%,
        var(--photo-edge) 100%);
  }
  .card-back { top: 521px; height: 343px; background: var(--card-white); }
  .brand {
    position: absolute; left: 72px; top: 92px; width: 170px;
    display: flex; align-items: center; gap: 9px;
  }
  .brand-dot {
    width: 22px; height: 22px; border-radius: 50%;
    background: var(--accent-blue); flex: none;
  }
  .brand-name {
    font-size: 25px; font-weight: 600; line-height: 1.05;
    color: var(--accent-purple);
  }
  .details { position: absolute; left: 300px; top: 57px; color: var(--ink); }
  .person-name { font-size: 20px; font-weight: 600; line-height: 27px; }
  .person-title { font-size: 16px; line-height: 20px; margin-bottom: 11px; }
  .address { font-size: 15.5px; font-weight: 600; line-height: 22px; }
  .contact-list { list-style: none; font-size: 16px; line-height: 21.5px; }
  .contact-label {
    display: inline-block; width: 22px;
    color: var(--accent-light); font-weight: 600;
  }
  .website { margin-top: 11px; font-size: 16px; color: var(--accent-light); }
  .colour-band { position: absolute; left: 0; bottom: 0; width: 100%; height: 12px; display: flex; }
  .band-light { width: 90px; background: var(--accent-light); }
  .band-blue { width: 210px; background: var(--accent-blue); }
  .band-purple { flex: 1; background: var(--accent-purple); }
</style>
</head>
<body>
<div class="stage">
  <section class="card card-front">
    <div class="front-photo" role="img" aria-label="Photo of a row of lightweight manual wheelchairs in charcoal and silver on a white backdrop"></div>
  </section>

  <section class="card card-back">
    <div class="brand">
      <span class="brand-dot"></span>
      <span class="brand-name">Glidewell Depot</span>
    </div>

    <div class="details">
      <p class="person-name">Sam Calder</p>
      <p class="person-title">Founder</p>
      <p class="address">Unit 8 14 Birch Street,<br>Wattlebrook NSW 2171, Australia</p>
      <ul class="contact-list">
        <li><span class="contact-label">t.</span>+61 2 9555 0142</li>
        <li><span class="contact-label">m.</span>+61 400 555 218</li>
        <li><span class="contact-label">f.</span>+61 2 9555 0187</li>
        <li><span class="contact-label">e.</span>info@glidewelldepot.com.au</li>
      </ul>
      <p class="website">www.glidewelldepot.com.au</p>
    </div>

    <div class="colour-band">
      <span class="band-light"></span>
      <span class="band-blue"></span>
      <span class="band-purple"></span>
    </div>
  </section>
</div>
</body>
</html>
```